Lumo Pharma Chinese Traditional Medicine Web Design

We need a web design for a new company based in Shanghai China called 'Lumo Pharma'. We develop Chinese traditional herbal medicine, including research and development, technical support service, manufacturing, . Also, there’s a small ratio of western medicine. Our goal is to contributing to a healthier future.

Target Market(s)

global,but mainly China

Industry/Entity Type

Pharmaceutical

Number of Pages Required

1 page

Font styles to use
Serif

Colors
e4daeb
cedeed
cadf82
eaf2ce
fbd4d5
fee3d4
fabb94
fee18a
b8a6cd

Requirements
Must have
• triditional Chinese elements, concept of herbal, health, value, better life for people..could be colourful but not more than 3 different colour..
Nice to have
• Style: simple, communicate traditional Chinese herbal medicine element, as well as modern technique..same as LOGO style..
Should not have
• please dont show more IT elements...

```html
<!DOCTYPE html>
<html lang="en">
<head>
<meta charset="utf-8">
<title>Lumo Pharma — Chinese Traditional Herbal Medicine</title>
<link rel="stylesheet" href="https://fonts.googleapis.com/css2?family=Playfair+Display:wght@600;700;800&family=Lora:wght@400;500;600;700&display=swap">
<style>
:root{
  --lavender:#b8a6cd;
  --lavender-soft:#e4daeb;
  --lime:#cadf82;
  --lime-soft:#eaf2ce;
  --lime-deep:#6f8a22;
  --peach:#fabb94;
  --peach-soft:#fee3d4;
  --peach-deep:#b8683a;
  --plum:#3a3145;
  --ink:#2a2530;
  --body:#5f5a66;
  --white:#ffffff;
}
*{box-sizing:border-box;margin:0;padding:0}
html,body{width:1200px;height:2670px;overflow:hidden;background:var(--white)}
body{font-family:"Lora",serif;color:var(--ink);position:relative}
.abs{position:absolute}
.btn{display:flex;align-items:center;justify-content:center;background:var(--lavender);color:var(--ink);font-family:"Lora",serif;font-weight:700;font-size:12px;letter-spacing:.3px;text-transform:uppercase;text-decoration:none}
.heading{font-family:"Playfair Display",serif;font-weight:700;color:var(--ink)}
.kicker{font-family:"Lora",serif;font-weight:400;color:var(--ink)}

/* header */
.site-header{position:absolute;left:0;top:0;width:1200px;height:77px;background:var(--white)}
.brand{position:absolute;left:96px;top:24px;display:flex;align-items:center;gap:10px}
.brand-mark{width:26px;height:26px;border-radius:50%;background:var(--lavender)}
.brand-name{font-family:"Lora",serif;font-weight:500;font-size:15px;color:var(--ink);letter-spacing:.5px}
.header-phone{position:absolute;right:93px;top:11px;display:flex;align-items:center;gap:6px;font-size:11.5px;color:var(--peach-deep)}
.header-phone .dot{width:25px;height:25px;border-radius:50%;background:var(--lavender);display:flex;align-items:center;justify-content:center}
.main-nav{position:absolute;right:93px;top:50px;display:flex;gap:36px;font-size:12px;color:var(--ink)}
.main-nav .active{color:var(--peach-deep)}

/* hero */
.hero-strip{left:0;top:77px;width:112px;height:523px;background:var(--lavender-soft)}
.hero-photo{left:469px;top:77px;width:731px;height:523px;background:linear-gradient(160deg,#3a2620 0%,#6b3426 35%,#b9b3ad 70%,#8c6a4e 100%)}
.hero-kicker{left:93px;top:230px;font-size:22px;letter-spacing:.5px}
.hero-title{left:93px;top:262px;font-family:"Playfair Display",serif;font-weight:800;font-size:45px;line-height:46px;color:var(--ink)}
.hero-title em{font-style:normal;color:var(--lime-deep)}
.hero-sub{left:93px;top:364px;font-size:18px;color:var(--ink)}
.hero-sub span{color:var(--peach-deep)}
.hero-btn{position:absolute;left:94px;top:403px;width:116px;height:36px}
.slider-prev{left:417px;top:563px;width:53px;height:37px;background:var(--lavender)}
.slider-next{left:470px;top:563px;width:52px;height:37px;background:var(--white)}

/* welcome */
.welcome-photo{left:0;top:625px;width:492px;height:388px;background:radial-gradient(ellipse at 70% 40%,#4a4632 0%,#7a6a48 20%,transparent 45%),linear-gradient(120deg,#d7a35d 0%,#e1b679 45%,#f7f2ea 75%,#ffffff 100%)}
.welcome-block{left:598px;top:652px;width:512px;display:flex;flex-direction:column;align-items:flex-start}
.welcome-kicker{font-size:19px}
.welcome-title{font-size:42px;line-height:50px;margin-top:2px}
.welcome-text{margin-top:12px;font-size:12.5px;line-height:21px;color:var(--body)}
.welcome-block .btn{margin-top:18px;width:104px;height:36px}

/* herbal */
.section-kicker{left:0;width:1200px;text-align:center;font-size:19px}
.section-title{left:0;width:1200px;text-align:center;font-size:42px;line-height:50px}
.herb-grid{left:93px;width:1014px;display:grid;grid-template-columns:repeat(4,245px);column-gap:11px}
.herb-card{height:300px;display:flex;flex-direction:column}
.herb-photo{width:245px;height:168px;flex:none}
.herb-name{margin-top:10px;font-family:"Lora",serif;font-size:17px;font-weight:600;color:var(--ink)}
.herb-text{margin-top:6px;font-size:11px;line-height:15.5px;color:var(--body)}
.herb-card .btn{margin-top:auto;width:104px;height:36px}

/* news */
.news-band{left:0;top:1808px;width:1200px;height:531px;background:var(--lime-soft)}
.news-grid{left:93px;top:1923px;width:1014px;display:grid;grid-template-columns:repeat(3,326px);column-gap:18px}
.news-card{height:360px;display:flex;flex-direction:column}
.news-photo{width:326px;height:208px;flex:none}
.news-date{margin-top:16px;font-size:10.5px;color:var(--peach-deep)}
.news-title{margin-top:8px;font-family:"Lora",serif;font-size:17px;font-weight:600;color:var(--ink)}
.news-text{margin-top:6px;font-size:12.5px;line-height:17.5px;color:var(--body)}
.news-card .btn{margin-top:auto;width:104px;height:36px}

/* contact */
.contact-band{left:0;top:2339px;width:1200px;height:331px;background:var(--plum)}
.contact-title{left:0;top:2368px;width:1200px;text-align:center;font-family:"Playfair Display",serif;font-weight:700;font-size:39px;color:var(--white)}
.contact-item{position:absolute;top:2439px}
.contact-icon{width:35px;height:35px;border-radius:50%;background:var(--lavender);display:flex;align-items:center;justify-content:center}
.contact-label{margin-top:12px;font-size:19px;font-weight:500;color:var(--white)}
.contact-value{margin-top:6px;font-size:13.5px;line-height:19px;color:var(--lavender-soft)}
.contact-divider{top:2476px;width:0;height:78px;border-left:1px dashed #6a5f78}
.agencies{left:520px;top:2570px;width:160px;height:32px;border-radius:16px;background:var(--lime);color:var(--ink);font-size:11.5px;font-weight:600;display:flex;align-items:center;justify-content:center}
.copyright{left:0;top:2621px;width:1200px;text-align:center;font-size:8.5px;color:var(--lavender-soft);letter-spacing:.2px}
.copyright span{color:var(--peach)}
</style>
</head>
<body>

<header class="site-header">
  <div class="brand"><span class="brand-mark"></span><span class="brand-name">LUMO PHARMA</span></div>
  <div class="header-phone">
    <span class="dot"><svg width="12" height="12" viewBox="0 0 24 24"><path fill="#2a2530" d="M6.6 10.8a15 15 0 0 0 6.6 6.6l2.2-2.2c.3-.3.7-.4 1-.2 1.1.4 2.3.6 3.6.6.6 0 1 .4 1 1V20c0 .6-.4 1-1 1A17 17 0 0 1 3 4c0-.6.4-1 1-1h3.5c.6 0 1 .4 1 1 0 1.3.2 2.5.6 3.6.1.3 0 .7-.2 1z"/></svg></span>
    +86 (021) 555 0147
  </div>
  <nav class="main-nav">
    <span class="active">Home</span><span>Company Overall</span><span>News</span><span>Products &amp; Services</span><span>Career</span><span>Contact Us</span>
  </nav>
</header>

<section class="hero">
  <div class="abs hero-strip"></div>
  <div class="abs hero-photo" role="img" aria-label="Interior of a traditional Chinese herbal pharmacy with wooden drawer cabinets and a marble counter"></div>
  <div class="abs kicker hero-kicker">CHINESE</div>
  <h1 class="abs hero-title">TRADITIONAL<br>HERBAL <em>MEDICINE</em></h1>
  <p class="abs hero-sub">LUMO Pharma is a <span>Pharmaceutical Company</span></p>
  <a class="btn hero-btn">Explore More</a>
  <div class="abs slider-prev"><svg width="53" height="37" viewBox="0 0 53 37"><path d="M34 18.5H19M24 13.5l-5 5 5 5" stroke="#2a2530" stroke-width="1.5" fill="none"/></svg></div>
  <div class="abs slider-next"><svg width="52" height="37" viewBox="0 0 52 37"><path d="M18 18.5h15M28 13.5l5 5-5 5" stroke="#2a2530" stroke-width="1.5" fill="none"/></svg></div>
</section>

<section class="welcome">
  <div class="abs welcome-photo" role="img" aria-label="Paper bag spilling dried herbal tea leaves"></div>
  <div class="abs welcome-block">
    <div class="kicker welcome-kicker">Welcome To</div>
    <h2 class="heading welcome-title">LUMO PHARMA</h2>
    <p class="welcome-text">Sed ut perspiciatis unde omnis iste natus error sit voluptatem accusantium doloremque laudantium, totam rem aperiam, eaque ipsa quae ab illo inventore veritatis et quasi architecto beatae vitae dicta sunt explicabo. Nemo enim ipsam voluptatem quia voluptas sit aspernatur aut odit aut fugit, sed quia consequuntur magni dolores eos qui ratione voluptatem sequi nesciunt. Neque porro quisquam est, qui dolorem ipsum quia dolor sit amet, consectetur, adipisci velit, sed quia non numquam eius modi tempora incidunt ut labore et dolore magnam aliquam quaerat voluptatem.</p>
    <a class="btn">Read More</a>
  </div>
</section>

<section class="herbal">
  <div class="abs kicker section-kicker" style="top:1009px">Chinese Traditional</div>
  <h2 class="abs heading section-title" style="top:1034px">HERBAL MEDICINE</h2>

  <div class="abs herb-grid" style="top:1116px">
    <article class="herb-card"><div class="herb-photo" role="img" aria-label="Assorted spices and herbs on a table" style="background:linear-gradient(135deg,#a89a88,#c9b8a0 50%,#8f7c66)"></div><h3 class="herb-name">Finibus Bonorum Malorum</h3><p class="herb-text">Sed ut perspiciatis unde omnis iste natus error sit voluptatem accusantium doloremque laudantium</p><a class="btn">View Details</a></article>
    <article class="herb-card"><div class="herb-photo" role="img" aria-label="Dried roots, cinnamon and star anise on dark stone" style="background:linear-gradient(135deg,#4d4b4a,#6a625a 55%,#3f3d3c)"></div><h3 class="herb-name">Finibus Bonorum Malorum</h3><p class="herb-text">Sed ut perspiciatis unde omnis iste natus error sit voluptatem accusantium doloremque laudantium</p><a class="btn">View Details</a></article>
    <article class="herb-card"><div class="herb-photo" role="img" aria-label="Herbal slices and goji berries on a violet background" style="background:linear-gradient(135deg,#d9b48a,#c48ad0 45%,#b57ac8 75%,#c74a3a)"></div><h3 class="herb-name">Finibus Bonorum Malorum</h3><p class="herb-text">Sed ut perspiciatis unde omnis iste natus error sit voluptatem accusantium doloremque laudantium</p><a class="btn">View Details</a></article>
    <article class="herb-card"><div class="herb-photo" role="img" aria-label="Cinnamon sticks, root slices and berries on grey" style="background:linear-gradient(135deg,#6a5e56,#77716c 50%,#5b5552)"></div><h3 class="herb-name">Finibus Bonorum Malorum</h3><p class="herb-text">Sed ut perspiciatis unde omnis iste natus error sit voluptatem accusantium doloremque laudantium</p><a class="btn">View Details</a></article>
  </div>

  <div class="abs herb-grid" style="top:1446px">
    <article class="herb-card"><div class="herb-photo" role="img" aria-label="Spoon of ground spice on burlap" style="background:linear-gradient(135deg,#a55a2e,#d49a5a 50%,#e2c39a)"></div><h3 class="herb-name">Finibus Bonorum Malorum</h3><p class="herb-text">Sed ut perspiciatis unde omnis iste natus error sit voluptatem accusantium doloremque laudantium</p><a class="btn">View Details</a></article>
    <article class="herb-card"><div class="herb-photo" role="img" aria-label="Bowls of dried herbs beside a blue book" style="background:linear-gradient(135deg,#2d3c66,#5a4b3e 50%,#8a7a60)"></div><h3 class="herb-name">Finibus Bonorum Malorum</h3><p class="herb-text">Sed ut perspiciatis unde omnis iste natus error sit voluptatem accusantium doloremque laudantium</p><a class="btn">View Details</a></article>
    <article class="herb-card"><div class="herb-photo" role="img" aria-label="Star anise and cinnamon on a wooden board" style="background:linear-gradient(135deg,#6e3c25,#c58d5b 50%,#a9693f)"></div><h3 class="herb-name">Finibus Bonorum Malorum</h3><p class="herb-text">Sed ut perspiciatis unde omnis iste natus error sit voluptatem accusantium doloremque laudantium</p><a class="btn">View Details</a></article>
    <article class="herb-card"><div class="herb-photo" role="img" aria-label="Teapot and bowl of dark berries with herbs" style="background:linear-gradient(135deg,#3e3826,#6a5a3a 50%,#b8a88e)"></div><h3 class="herb-name">Finibus Bonorum Malorum</h3><p class="herb-text">Sed ut perspiciatis unde omnis iste natus error sit voluptatem accusantium doloremque laudantium</p><a class="btn">View Details</a></article>
  </div>
</section>

<section class="news">
  <div class="abs news-band"></div>
  <h2 class="abs heading section-title" style="top:1858px">RECENT NEWS</h2>
  <div class="abs news-grid">
    <article class="news-card"><div class="news-photo" role="img" aria-label="Stone mortar filled with dried herbs" style="background:linear-gradient(135deg,#2a1e16,#6a4a30 50%,#a07850)"></div><p class="news-date">18th April, 2020</p><h3 class="news-title">The standard Lorem Ipsum passage</h3><p class="news-text">Sed ut perspiciatis unde omnis iste natus error sit voluptatem accusantium doloremque</p><a class="btn">View Details</a></article>
    <article class="news-card"><div class="news-photo" role="img" aria-label="Pharmacist at a herbal drawer cabinet counter" style="background:linear-gradient(135deg,#b8ae90,#d8ceb4 50%,#8a6a4a)"></div><p class="news-date">18th April, 2020</p><h3 class="news-title">The standard Lorem Ipsum passage</h3><p class="news-text">Sed ut perspiciatis unde omnis iste natus error sit voluptatem accusantium doloremque</p><a class="btn">View Details</a></article>
    <article class="news-card"><div class="news-photo" role="img" aria-label="Bowls of herbs and flowers on a wooden table" style="background:linear-gradient(135deg,#3a2a24,#7a4a3e 50%,#5a3a2a)"></div><p class="news-date">18th April, 2020</p><h3 class="news-title">The standard Lorem Ipsum passage</h3><p class="news-text">Sed ut perspiciatis unde omnis iste natus error sit voluptatem accusantium doloremque</p><a class="btn">View Details</a></article>
  </div>
</section>

<footer class="contact">
  <div class="abs contact-band"></div>
  <h2 class="abs contact-title">CONTACT US</h2>

  <div class="contact-item" style="left:295px">
    <div class="contact-icon"><svg width="14" height="14" viewBox="0 0 24 24"><path fill="#2a2530" d="M12 2a7 7 0 0 0-7 7c0 5 7 13 7 13s7-8 7-13a7 7 0 0 0-7-7zm0 9.5A2.5 2.5 0 1 1 12 6.5a2.5 2.5 0 0 1 0 5z"/></svg></div>
    <div class="contact-label">Address:</div>
    <div class="contact-value">88 Lorem Ipsum Road Jing'an,<br>Shanghai China</div>
  </div>
  <div class="abs contact-divider" style="left:529px"></div>
  <div class="contact-item" style="left:568px">
    <div class="contact-icon"><svg width="13" height="13" viewBox="0 0 24 24"><path fill="#2a2530" d="M6.6 10.8a15 15 0 0 0 6.6 6.6l2.2-2.2c.3-.3.7-.4 1-.2 1.1.4 2.3.6 3.6.6.6 0 1 .4 1 1V20c0 .6-.4 1-1 1A17 17 0 0 1 3 4c0-.6.4-1 1-1h3.5c.6 0 1 .4 1 1 0 1.3.2 2.5.6 3.6.1.3 0 .7-.2 1z"/></svg></div>
    <div class="contact-label">Phone:</div>
    <div class="contact-value">+86 (021) 555 0147</div>
  </div>
  <div class="abs contact-divider" style="left:725px"></div>
  <div class="contact-item" style="left:766px">
    <div class="contact-icon"><svg width="14" height="14" viewBox="0 0 24 24"><path fill="#2a2530" d="M3 6h18v12H3z"/><path d="M3 6l9 7 9-7" stroke="#b8a6cd" stroke-width="2" fill="none"/></svg></div>
    <div class="contact-label">Email:</div>
    <div class="contact-value">hello@lumopharma.com</div>
  </div>

  <div class="abs agencies">OTHER AGENCIES</div>
  <p class="abs copyright">COPYRIGHT © 2020 <span>LUMO PHARMA</span>. ALL RIGHTS RESERVED.</p>
</footer>

</body>
</html>
```